We need a business card design for a Dubai based company .

We need a business card for a Dubai based company called "Zernova Smoking Requisites Trading LLC". We mainly import Flavoured Tobacco products and Charcoal which is used for smoking in a Hookah/Shisha and distribute to the wholesalers and retailers. Logo file is attached herewith.

```html
<!DOCTYPE html>
<html lang="en">
<head>
<meta charset="utf-8">
<title>Zernova Smoking Requisites Trading LLC – Business Card</title>
<link href="https://fonts.googleapis.com/css2?family=Michroma&display=swap" rel="stylesheet">
<style>
  :root{
    --bg:#ece8e2;
    --card:#ffffff;
    --red:#a3222a;
    --ink:#1a1a1a;
    --grey:#8f8f8f;
    --font:"Michroma", sans-serif;
  }
  *{box-sizing:border-box;margin:0;padding:0}
  html,body{width:1200px;height:1200px;overflow:hidden;background:var(--bg);font-family:var(--font)}
  .sheet{position:relative;width:1200px;height:1200px}
  .card{position:absolute;left:170px;width:860px;height:490px;background:var(--card);box-shadow:0 6px 18px rgba(0,0,0,.12);overflow:hidden}
  .card--front{top:80px}
  .card--back{top:630px}
  .rule-v{position:absolute;top:0;bottom:0;width:5px;background:var(--red)}

  /* front */
  .front .rule-v.outer{left:40px}
  .front .rule-v.inner{left:112px}
  .identity{position:absolute;left:150px;top:120px;color:var(--red)}
  .identity__name{font-size:40px;letter-spacing:2px;line-height:1}
  .identity__role{font-size:20px;letter-spacing:2px;margin-top:6px}
  .identity__rule{position:absolute;left:150px;top:220px;width:360px;height:6px;background:var(--red)}
  .contacts{position:absolute;left:78px;top:265px;list-style:none}
  .contacts li{display:flex;align-items:center;height:54px}
  .contacts svg{width:40px;height:40px;flex:none;background:var(--card);border-radius:50%}
  .contacts span{margin-left:52px;font-size:17px;letter-spacing:2px;color:var(--ink)}

  .company{position:absolute;text-align:center;white-space:nowrap}
  .company__name{color:var(--ink);line-height:1}
  .company__tagline{color:var(--red);display:block}
  .front .company{right:50px;top:100px}
  .front .company__name{font-size:32px;letter-spacing:2px}
  .front .company__tagline{font-size:8px;letter-spacing:1.6px;margin-top:12px}
  .scene-art{position:absolute;left:560px;top:240px;width:270px;height:200px;border-radius:40px 40px 10px 10px;background:linear-gradient(180deg,#a3a3a3,var(--grey))}

  /* back */
  .back .rule-v.l1{left:42px}
  .back .rule-v.l2{left:112px}
  .back .rule-v.r1{right:112px}
  .back .rule-v.r2{right:42px}
  .back .company{left:50%;top:50%;transform:translate(-50%,-50%)}
  .back .company__name{font-size:50px;letter-spacing:4px}
  .back .company__tagline{font-size:11.5px;letter-spacing:3px;margin-top:16px}
</style>
</head>
<body>
<main class="sheet">

  <section class="card card--front front">
    <div class="rule-v outer"></div>
    <div class="rule-v inner"></div>

    <div class="identity">
      <div class="identity__name">YOUR NAME</div>
      <div class="identity__role">CEO / DIRECTOR</div>
    </div>
    <div class="identity__rule"></div>

    <ul class="contacts">
      <li>
        <svg viewBox="0 0 40 40" aria-hidden="true"><circle cx="20" cy="20" r="17" fill="#fff" stroke="var(--red)" stroke-width="2.5"/><circle cx="20" cy="20" r="12.5" fill="none" stroke="var(--red)" stroke-width="1.5"/><path d="M15 13c1-1 2-1 2.5 0l1.5 3c.3.7 0 1.2-.6 1.6l-1 .7c.8 2 2.3 3.6 4.3 4.5l.7-1c.4-.6 1-.8 1.6-.5l3 1.5c.9.5.9 1.5 0 2.5-1.5 1.6-4 1.4-6.5-.3-2.6-1.8-4.6-4.3-5.6-6.9-.8-2-.7-3.8.1-5.1z" fill="var(--red)"/></svg>
        <span>555-333-777-55</span>
      </li>
      <li>
        <svg viewBox="0 0 40 40" aria-hidden="true"><circle cx="20" cy="20" r="17" fill="#fff" stroke="var(--red)" stroke-width="2.5"/><circle cx="20" cy="20" r="12.5" fill="none" stroke="var(--red)" stroke-width="1.5"/><rect x="16" y="12" width="8" height="16" rx="1.5" fill="none" stroke="var(--red)" stroke-width="1.6"/><circle cx="20" cy="25.5" r=".9" fill="var(--red)"/></svg>
        <span>444-333-777-55</span>
      </li>
      <li>
        <svg viewBox="0 0 40 40" aria-hidden="true"><circle cx="20" cy="20" r="17" fill="#fff" stroke="var(--red)" stroke-width="2.5"/><circle cx="20" cy="20" r="12.5" fill="none" stroke="var(--red)" stroke-width="1.5"/><rect x="13" y="15" width="14" height="10" fill="none" stroke="var(--red)" stroke-width="1.6"/><path d="M13 15l7 6 7-6M13 25l5-5M27 25l-5-5" fill="none" stroke="var(--red)" stroke-width="1.4"/></svg>
        <span>your@mailbox.com</span>
      </li>
      <li>
        <svg viewBox="0 0 40 40" aria-hidden="true"><circle cx="20" cy="20" r="17" fill="#fff" stroke="var(--red)" stroke-width="2.5"/><circle cx="20" cy="20" r="12.5" fill="none" stroke="var(--red)" stroke-width="1.5"/><circle cx="20" cy="20" r="8" fill="none" stroke="var(--red)" stroke-width="1.3"/><ellipse cx="20" cy="20" rx="3.5" ry="8" fill="none" stroke="var(--red)" stroke-width="1.2"/><path d="M12 20h16M13.5 16h13M13.5 24h13" stroke="var(--red)" stroke-width="1.1"/></svg>
        <span>www.yourweb.com</span>
      </li>
    </ul>

    <div class="company">
      <div class="company__name">Zernova</div>
      <span class="company__tagline">SMOKING REQUISITES TRADING LLC</span>
    </div>

    <div class="scene-art" role="img" aria-label="Grey silhouette of a man sitting on the floor beside a hookah"></div>
  </section>

  <section class="card card--back back">
    <div class="rule-v l1"></div>
    <div class="rule-v l2"></div>
    <div class="rule-v r1"></div>
    <div class="rule-v r2"></div>

    <div class="company">
      <div class="company__name">Zernova</div>
      <span class="company__tagline">SMOKING REQUISITES TRADING LLC</span>
    </div>
  </section>

</main>
</body>
</html>
```